Quiet Hollow - New Product needs a Label

We need a package label for a new project that will come to market soon. The company is based in Canada and will need to show 'Made in Canada' with a Canadian flag.

The product is called Quiet Hollow. It is an odour eliminator. It will be in a dark brown plastic container that can be opened and left open in a room.

It can be used to help eliminate a number of different types of smoke; cigarette, pot or even fireplace smoke. We believe that 'no one should know what you smoke'.

We would like to see designs that reflect the intent of the product - to cover smoke. So far we've only thought that smokey colours like smokey green, smokey lavender and smokey grey or other grey tone colours would make sense. Update: I have removed the image that I 'doodled' on my own because I think it's been taken too literally. Please give me a fresh look at what an odor eliminator image could be.

Label dimensions are 11.25"x2.25"
Key wording:

Product Name: Quiet Hollow
Tag line: No one needs to know what you smoke
Also needs to include:
Directions
Remove the lid and place the container in any room where smoke is present. The contents will evaporate, neutralizing odours.

Net Wt. 14 0z. - 400 G
A spot for adding a bar code for scanners

Target Market(s)

Cigarette smokers / pot smokers / people with fire places or people who share a home with any of those categories

Requirements
Must have
• a label that fits the dimensions 11.25"x2.25" and the text / components outlined in the description
Nice to have
• A bit of humour, a sense of natural products

```html
<!DOCTYPE html>
<html lang="en">
<head>
<meta charset="utf-8">
<title>Quiet Hollow – Odour Eliminator Label</title>
<link href="https://fonts.googleapis.com/css2?family=Montserrat:wght@400;500;700&family=Archivo+Black&display=swap" rel="stylesheet">
<style>
  :root{
    --page:#f2f3f5;
    --ink:#3a3a3c;
    --ink-soft:#5a5a5d;
    --label-white:#ffffff;
    --smoke:#b9babd;
    --smoke-dark:#8e8f93;
    --leaf:#c6dcc2;
    --badge:#e1262d;
    --pill-text:#ffffff;
  }
  *{box-sizing:border-box;margin:0;padding:0}
  html,body{width:1200px;height:1058px;overflow:hidden}
  body{background:var(--page);font-family:"Montserrat",sans-serif;color:var(--ink);position:relative}

  .label{
    position:absolute;left:40px;top:416px;width:1120px;height:225px;overflow:hidden;
    background:
      radial-gradient(ellipse 260px 70px at 210px 180px, rgba(142,143,147,.55), transparent 70%),
      radial-gradient(ellipse 300px 60px at 620px 150px, rgba(142,143,147,.45), transparent 70%),
      radial-gradient(ellipse 220px 80px at 560px 40px, rgba(185,186,189,.45), transparent 70%),
      radial-gradient(ellipse 260px 70px at 950px 200px, rgba(142,143,147,.45), transparent 70%),
      radial-gradient(ellipse 180px 60px at 60px 210px, rgba(142,143,147,.5), transparent 70%),
      var(--label-white);
    box-shadow:0 2px 6px rgba(0,0,0,.25);
  }

  .directions{position:absolute;left:86px;top:48px;width:200px;text-align:center;font-size:11.5px;line-height:13.5px;font-weight:500}

  .barcode-spot{position:absolute;left:80px;top:141px;width:121px;height:54px;background:var(--ink)}

  .origin-badge{position:absolute;left:217px;top:129px;width:80px;height:80px;border-radius:50%;background:var(--badge);border:4px solid var(--label-white);box-shadow:0 0 0 1px var(--badge)}

  .leaf-art{position:absolute;left:321px;top:7px;width:178px;height:212px;
    background:radial-gradient(ellipse at 50% 70%, rgba(198,220,194,.7), rgba(198,220,194,.15) 70%, transparent 72%)}

  .brand{position:absolute;left:478px;top:34px;width:232px;text-align:center}
  .brand-name{font-weight:700;font-size:46px;line-height:46px;letter-spacing:1px;color:var(--ink)}
  .brand-type{margin-top:8px;border-top:1.5px solid var(--ink);border-bottom:1.5px solid var(--ink);font-size:17px;line-height:24px;font-weight:400;letter-spacing:.5px}

  .tagline{position:absolute;left:391px;top:174px;width:336px;height:17px;border-radius:9px 9px 2px 2px;background:var(--ink);color:var(--pill-text);font-size:11px;font-weight:500;line-height:17px;text-align:center}
  .net-weight{position:absolute;left:391px;top:192px;width:336px;text-align:center;font-size:10px;line-height:14px}

  .nutrition{position:absolute;left:810px;top:35px;width:265px;height:156px;border:1px solid var(--ink-soft);padding:2px 3px;font-size:5.5px;line-height:7px;color:var(--ink)}
  .nutrition-title{font-family:"Archivo Black",sans-serif;font-size:19px;line-height:22px}
  .row{display:flex;justify-content:space-between;border-top:.5px solid var(--smoke-dark)}
  .row.thick{border-top:4px solid var(--ink)}
  .row.bold{font-weight:700}
  .row.indent span:first-child{padding-left:8px}
  .row.indent2 span:first-child{padding-left:16px}
  .calories{font-weight:700;font-size:11px;line-height:14px}
  .calories b{font-size:15px}
</style>
</head>
<body>
  <section class="label">
    <p class="directions">Directions<br>Remove the lid and place the container in any room where smoke is present. The contents will evaporate, neutralizing odours.</p>
    <div class="barcode-spot" aria-label="Space for barcode"></div>
    <div class="origin-badge" aria-label="Made in Canada badge"></div>
    <div class="leaf-art" role="img" aria-label="Faint green leaf illustration"></div>

    <div class="brand">
      <h1 class="brand-name">QUIET<br>HOLLOW</h1>
      <p class="brand-type">ODOUR ELIMINATOR</p>
    </div>

    <p class="tagline">NO ONE NEEDS TO KNOW WHAT YOU SMOKE</p>
    <p class="net-weight">Net Wt. 14 0z. - 400 G</p>

    <div class="nutrition">
      <div class="nutrition-title">Nutrition Facts</div>
      <div class="row"><span>4 servings per container/6 raciones por envase</span></div>
      <div class="row bold" style="border-top:none"><span>Serving size</span><span>1 cup/1 taza (180g)</span></div>
      <div class="row thick"><span>Amount per serving/Cantidad por porción</span></div>
      <div class="row calories" style="border-top:none"><span>Calories/Calorías</span><b>245</b></div>
      <div class="row"><span></span><span>% Daily Value*/% Valor diario*</span></div>
      <div class="row"><span><b>Total Fat/Grasa total</b> 12g</span><b>14%</b></div>
      <div class="row indent"><span>Saturated Fat/Grasa Saturada 2g</span><b>10%</b></div>
      <div class="row indent"><span><i>Trans Fat/Grasa Trans</i> 0g</span><span></span></div>
      <div class="row"><span><b>Cholesterol/Colesterol</b> 8mg</span><b>3%</b></div>
      <div class="row"><span><b>Sodium/Sodio</b> 210mg</span><b>9%</b></div>
      <div class="row"><span><b>Total Carbohydrate/Carbohidrato Total</b> 34g</span><b>12%</b></div>
      <div class="row indent"><span>Dietary Fiber/Fibra Dietética 7g</span><b>25%</b></div>
      <div class="row indent"><span>Total Sugars/Azúcares Totales 5g</span><span></span></div>
      <div class="row indent2"><span>Includes 4g Added Sugars/Incluye 4 g de azúcares añadidos</span><b>8%</b></div>
    </div>
  </section>
</body>
</html>
```